Canadian printing equipment Manufacturer needs a brochure design

We want to make the graphic design of our brochure more attractive (attached Brochure Variline.pdf). But it should still match with our web-design (www.morvalprint.com). The texts and photos will stay as it. We need to make all the photos looking consistently all over the brochure as well as we need to change “sandwiches” design (pages 4-5 and 8-9) for more modern. I also attached a brochure of one of our competitor to compare (Brochure_Competitor.pdf). The product is different types of equipment that produce the labels (all labels you see on the bottles of beverages, cosmetics etc. Big machines approx 10-20 m long and 2-5 m hight depending of configuration. We sell worldwide (USA, Canada, all Europe, Japan, Russia and more else). I have this file in ai but can not download here because of its big size.

Reason: not sure for my decision yet

Target Market(s)

Label Printing compagnies

Industry/Entity Type

Graphic Design

Colors
0255a3
ffc214
d3d3d3
ffffff

Requirements
Must have
• Elegant modern look

```html
<!DOCTYPE html>
<html lang="en">
<head>
<meta charset="utf-8">
<title>Morval – Latest Technologies spread</title>
<link href="https://fonts.googleapis.com/css2?family=Montserrat:wght@300;400;600&display=swap" rel="stylesheet">
<style>
:root{
  --blue:#0255a3;
  --blue-deep:#1f3fb8;
  --yellow:#ffc214;
  --grey:#d3d3d3;
  --grey-soft:#efefef;
  --white:#ffffff;
  --ink:#4a4a4a;
  --red:#f04a23;
  --sky:#9fd0f2;
  --bg:#e4e4e4;
}
*{margin:0;padding:0;box-sizing:border-box}
html,body{width:1200px;height:1011px;overflow:hidden;background:var(--bg);font-family:"Montserrat",sans-serif;color:var(--ink)}
.spread{position:absolute;left:0;top:82px;width:1200px;height:848px;display:flex;box-shadow:0 10px 30px rgba(0,0,0,.15)}
.page{position:relative;width:600px;height:848px;background:var(--white);overflow:hidden}
.page svg.bands{position:absolute;inset:0}
.brand{position:absolute;left:30px;top:34px;display:flex;align-items:center;gap:8px}
.brand-dot{width:30px;height:30px;border-radius:50%;background:var(--blue-deep)}
.brand-name{font-weight:600;font-size:22px;color:var(--blue-deep);line-height:1}
.brand-tag{position:absolute;left:68px;top:62px;font-size:7px;color:var(--blue-deep)}
.band-title{position:absolute;color:var(--white);font-weight:300;font-size:26px;letter-spacing:1px;white-space:nowrap;line-height:1}
.section-head{position:absolute;font-weight:400;font-size:15px;color:var(--blue);letter-spacing:1px;text-transform:uppercase}
.body-text{position:absolute;font-size:9.5px;line-height:1.35;color:var(--ink)}
.layers{position:absolute}
.layer-label{position:absolute;font-size:8px;color:var(--ink);white-space:nowrap}
.layer-label.strong{font-weight:600}
.layer-title{position:absolute;font-size:10px;color:var(--ink);white-space:nowrap}
.features-head{position:absolute;font-size:14px;color:var(--blue);text-transform:uppercase;letter-spacing:1px}
.features{position:absolute;list-style:none;font-size:10px;line-height:1.45}
.features li{padding-left:11px;position:relative}
.features li::before{content:"";position:absolute;left:0;top:4px;width:6px;height:6px;background:var(--yellow)}
.photo{position:absolute}
</style>
</head>
<body>
<div class="spread">

  <section class="page page-left">
    <svg class="bands" width="600" height="848" viewBox="0 0 600 848">
      <polygon points="200,40 600,40 600,100 182,100" fill="var(--blue-deep)"/>
      <polygon points="170,40 186,40 168,100 152,100" fill="var(--yellow)"/>
      <polygon points="189,40 195,40 177,100 171,100" fill="var(--blue)"/>
      <path d="M0,400 C200,410 400,440 600,500 L600,848 L0,848 Z" fill="var(--grey-soft)"/>
      <path d="M0,380 C200,390 400,420 600,480 L600,500 C400,440 200,410 0,400 Z" fill="var(--yellow)"/>
      <polygon points="340,560 600,525 600,848 340,848" fill="var(--blue-deep)"/>
      <polygon points="355,578 600,548 600,835 355,835" fill="var(--yellow)"/>
    </svg>
    <div class="brand"><span class="brand-dot"></span><span class="brand-name">Morval</span></div>
    <div class="brand-tag">converting equipment</div>
    <div class="band-title" style="left:222px;top:57px">LATEST TECHNOLOGIES</div>

    <div class="section-head" style="left:60px;top:128px">Slimliner™</div>
    <p class="body-text" style="left:60px;top:150px;width:480px">The Slimliner™ technology using film or paper-based substrates is a simple option that could be added to the existing Variline technology. Designed to reduce substantially the release liner waste, the Slimliner™ technology concept is unique and simple. PS labels are manufactured from raw material to the finished product down to a totally recyclable 12 micron (.48 mil) PET release liner or 30 gsm (20 lbs) paper release liner.</p>

    <div class="layer-title" style="left:60px;top:228px">Standard PS material</div>
    <svg class="layers" style="left:60px;top:244px" width="130" height="46">
      <rect x="0" y="0" width="120" height="8" fill="var(--sky)"/>
      <rect x="0" y="12" width="120" height="8" fill="var(--red)"/>
      <rect x="0" y="24" width="120" height="8" fill="var(--yellow)"/>
      <rect x="0" y="36" width="120" height="8" fill="var(--grey)"/>
    </svg>
    <div class="layer-label" style="left:196px;top:243px">Facestock</div>
    <div class="layer-label" style="left:196px;top:255px">Adhesive</div>
    <div class="layer-label" style="left:196px;top:267px">Silicone</div>
    <div class="layer-label strong" style="left:196px;top:279px">Liner: PET 30 mic<br>or Paper 58gsm</div>

    <div class="layer-title" style="left:440px;top:228px">Slimliner™</div>
    <svg class="layers" style="left:440px;top:244px" width="130" height="40">
      <rect x="0" y="0" width="120" height="8" fill="var(--yellow)"/>
      <rect x="0" y="12" width="120" height="8" fill="var(--red)"/>
      <rect x="0" y="24" width="120" height="8" fill="var(--sky)"/>
      <rect x="0" y="34" width="120" height="4" fill="var(--grey)"/>
    </svg>
    <div class="layer-label" style="left:340px;top:243px">Facestock</div>
    <div class="layer-label" style="left:340px;top:255px">Adhesive</div>
    <div class="layer-label" style="left:340px;top:267px">Silicone</div>
    <div class="layer-label strong" style="left:340px;top:279px">Liner: PET 12 mic<br>or Paper 30gsm</div>

    <div class="section-head" style="left:60px;top:310px">Tracecut</div>
    <p class="body-text" style="left:60px;top:331px;width:470px">The Tracecut is a heavy duty module for precise die-cutting including W-type anti-deflecting system and die equalizer system. This module was designed to die cut on Slimliner without any die-cutting mark.</p>

    <div class="features-head" style="left:70px;top:420px">Features</div>
    <ul class="features" style="left:70px;top:446px;width:250px">
      <li>Substantial savings — down to a 12 micron (.48mil) clear PET or paper 30 gsm (20 lbs) release liner</li>
      <li>Environmentally friendly — less waste, recyclable liner</li>
      <li>Mark free die-cutting</li>
      <li>Adaptable to existing Variline technology and/or other existing presses</li>
      <li>Could be a stand-alone equipment</li>
      <li>Designed for high speed application up to 225m/min (750 fpm)</li>
      <li>Less waste</li>
      <li>More labels / roll — less roll change</li>
      <li>Use conventional labeling equipment</li>
      <li>Use a conventional magnetic die cylinder</li>
      <li>Use a standard room temperature die</li>
      <li>Diameter expansion control system</li>
      <li>Fast change-over with drawer system</li>
    </ul>

    <div class="photo" role="img" aria-label="Photos of labelled beverage bottles and a label press line" style="left:370px;top:596px;width:230px;height:226px;background:linear-gradient(135deg,#8a8f96,#3f5a3a 55%,#2c3f8a)"></div>
  </section>

  <section class="page page-right">
    <svg class="bands" width="600" height="848" viewBox="0 0 600 848">
      <polygon points="196,110 600,110 600,175 176,175" fill="var(--blue-deep)"/>
      <polygon points="164,110 182,110 162,175 144,175" fill="var(--yellow)"/>
      <path d="M0,440 C200,445 400,460 600,500 L600,848 L0,848 Z" fill="var(--grey-soft)"/>
      <path d="M0,420 C200,425 400,440 600,480 L600,500 C400,460 200,445 0,440 Z" fill="var(--yellow)"/>
      <polygon points="360,640 600,640 600,848 300,848" fill="var(--blue-deep)"/>
      <rect x="560" y="640" width="40" height="18" fill="var(--yellow)"/>
    </svg>
    <div class="band-title" style="left:210px;top:129px">LATEST TECHNOLOGIES</div>

    <div class="section-head" style="left:90px;top:198px">Linerless Solutions</div>
    <p class="body-text" style="left:90px;top:220px;width:470px">Morval developed several years ago a linerless technology that no longer uses release liners as a carrier. In fact, there is no release liner during our printing process. For years, linerless technology was strictly used for hand applied applications. Morval develops various technologies for linerless labels to meet the market needs such as the possibility of automatic application.</p>

    <div class="layer-title" style="left:70px;top:298px">Standard PS material</div>
    <svg class="layers" style="left:70px;top:314px" width="130" height="46">
      <rect x="0" y="0" width="120" height="8" fill="var(--sky)"/>
      <rect x="0" y="12" width="120" height="8" fill="var(--red)"/>
      <rect x="0" y="24" width="120" height="8" fill="var(--yellow)"/>
      <rect x="0" y="36" width="120" height="8" fill="var(--grey)"/>
    </svg>
    <div class="layer-label" style="left:206px;top:313px">Facestock</div>
    <div class="layer-label" style="left:206px;top:325px">Adhesive</div>
    <div class="layer-label" style="left:206px;top:337px">Silicone</div>
    <div class="layer-label strong" style="left:206px;top:349px">Liner: PET 30 mic<br>or Paper 58gsm</div>

    <div class="layer-title" style="left:420px;top:330px">LINERLESS</div>
    <svg class="layers" style="left:420px;top:346px" width="130" height="60">
      <rect x="0" y="0" width="120" height="8" fill="var(--yellow)"/>
      <rect x="0" y="12" width="120" height="8" fill="var(--sky)"/>
      <rect x="0" y="24" width="120" height="8" fill="var(--red)"/>
      <path d="M0,48 L14,48 M8,43 L14,48 L8,53" stroke="var(--ink)" stroke-width="1.5" fill="none"/>
    </svg>
    <div class="layer-label" style="left:340px;top:345px">Silicone</div>
    <div class="layer-label" style="left:340px;top:357px">Clear Film o Paper</div>
    <div class="layer-label" style="left:340px;top:369px">Adhesive</div>
    <div class="layer-label" style="left:548px;top:345px">Printing</div>
    <div class="layer-label" style="left:548px;top:369px">Printing</div>
    <div class="layer-label" style="left:440px;top:390px">Web direction</div>

    <div class="features-head" style="left:110px;top:456px">Features</div>
    <ul class="features" style="left:110px;top:482px;width:220px">
      <li>Substantial savings — no more liner</li>
      <li>Less waste</li>
      <li>Designed for high speed automatic application</li>
      <li>Environmentally friendly</li>
      <li>Front and back printing</li>
      <li>Double labels quantity per roll</li>
      <li>More labels / roll — less roll change</li>
      <li>No compromise on label shape on existing labels</li>
      <li>Possibility of pattern adhesive application</li>
    </ul>

    <div class="photo" role="img" aria-label="Photo of a printed linerless label roll" style="left:120px;top:740px;width:150px;height:50px;background:linear-gradient(90deg,#3a1f10,#b0341c)"></div>
    <div class="photo" role="img" aria-label="Photo of printed label rolls and linerless roll samples" style="left:385px;top:672px;width:200px;height:150px;background:linear-gradient(135deg,#e9e4d6,#bfb7a3 50%,#8c5a2e)"></div>
  </section>

</div>
</body>
</html>
```